Sheep ranch business card design

We need a business card design for our farm. We do all things sheep. We run Babydoll southdown sheep and use their fiber and meat. In the spring the lambs are sold. We shear them for their wool to make dryer balls, roving, and yarn which we sell. We also lease the sheep out to organic vineyards in the winter time to help them convert their weeds and cover crops to manure so they don't have to use tractors and tillers to mow and compact soil. Fennick Ranch also breeds Kangals which are livestock guard dogs that live with and protect the sheep. We also run a small herd of jersey cows, chickens, and bees but the sheep enterprise is the focal point. I would like to see the design use more earth tones and natural colors and have the feel of a modern and hip farm. I would also like our attached fennick ranch image to be used. The font family is dalle for our logo. That font can be used or something to compliment it. The attached pictures can be used as well but they are not necessary. One fennick ranch upload is in psd and one is in jpeg. Thank You and we look forward to seeing your work.
Updates

So many great designs. Not looking for anything "western." Font, design, or otherwise.

Industry/Entity Type

Livestock

Contact Information for Business Card

Fennick Ranch
Corin Fennick
www.fennickranch-example.com
fennickranch@mailbox-example.com
phone: 555 310-7282

```html
<!DOCTYPE html>
<html lang="en">
<head>
<meta charset="utf-8">
<title>Fennick Ranch – Business Cards</title>
<link rel="stylesheet" href="https://fonts.googleapis.com/css2?family=Roboto+Condensed:wght@400;700&display=swap">
<style>
  :root {
    --bg: #e7e2da;
    --peach: #f3cf9f;
    --peach-light: #f8dfbb;
    --rust: #8a3a2c;
    --maroon: #6b2725;
    --cream: #f6e6c8;
    --ink-light: #eadfcd;
    --earth-dark: #3b2b1d;
    --earth-mid: #5b4530;
    --field-green: #8d8a4a;
    --fleece: #d9c29b;
  }
  * { box-sizing: border-box; margin: 0; padding: 0; }
  html, body { width: 1200px; height: 872px; overflow: hidden; }
  body {
    background: var(--bg);
    font-family: "Roboto Condensed", "Arial Narrow", sans-serif;
    position: relative;
  }
  .card {
    position: absolute;
    top: 286px;
    width: 520px;
    height: 300px;
    overflow: hidden;
    box-shadow: 0 6px 18px rgba(0,0,0,.18);
  }
  .card--earth { left: 60px; }
  .card--meadow { left: 620px; }

  .card__frame { position: absolute; inset: 0; width: 100%; height: 100%; }
  .card__photo { position: absolute; }

  /* Earth card */
  .card--earth .card__photo {
    inset: 0;
    background: linear-gradient(160deg, var(--earth-mid) 0%, var(--earth-dark) 55%, #4a3624 100%);
  }
  .brand-name {
    position: absolute;
    font-weight: 700;
    letter-spacing: 3px;
    text-transform: uppercase;
    white-space: nowrap;
  }
  .card--earth .brand-name { right: 28px; top: 22px; font-size: 24px; line-height: 28px; color: var(--rust); }
  .card--earth .contact {
    position: absolute; right: 30px; top: 88px; text-align: right; color: var(--ink-light);
  }
  .card--earth .person {
    font-size: 28px; font-weight: 400; padding-bottom: 6px;
    border-bottom: 2px solid var(--ink-light); margin-bottom: 14px;
  }
  .card--earth .detail { font-size: 15px; line-height: 26px; }
  .card--earth .website {
    position: absolute; left: 26px; bottom: 18px; font-size: 17px; line-height: 22px;
    font-weight: 700; color: var(--rust); white-space: nowrap;
  }

  /* Meadow card */
  .card--meadow .card__photo {
    left: 0; right: 0; top: 62px; bottom: 54px;
    background: linear-gradient(100deg, #6e6a3a 0%, var(--field-green) 30%, #b9a677 60%, var(--fleece) 100%);
  }
  .card--meadow .brand-name { right: 26px; top: 16px; font-size: 28px; color: var(--cream); }
  .card--meadow .person {
    position: absolute; right: 26px; top: 76px; font-size: 30px; font-weight: 700; color: #fff;
  }
  .card--meadow .detail-bar {
    position: absolute; right: 26px; height: 28px; line-height: 28px; padding: 0 14px;
    background: var(--cream); color: var(--maroon); font-size: 15px; white-space: nowrap;
  }
  .card--meadow .detail-bar--phone { top: 124px; width: 250px; }
  .card--meadow .detail-bar--email { top: 160px; width: 320px; }
  .card--meadow .website {
    position: absolute; left: 24px; bottom: 15px; font-size: 20px; font-weight: 700; color: var(--cream);
  }
</style>
</head>
<body>

<section class="card card--earth">
  <div class="card__photo" role="img" aria-label="Photograph of a woolly Babydoll sheep in dark earthy tones"></div>
  <svg class="card__frame" viewBox="0 0 520 300" aria-hidden="true">
    <path d="M258 0 H520 V72 H268 Q254 72 250 60 L240 16 Q237 0 258 0 Z" fill="var(--peach)"/>
    <path d="M0 228 H318 Q334 228 340 242 L346 256 Q352 270 368 270 H520 V300 H0 Z" fill="var(--peach-light)"/>
    <rect x="0" y="0" width="12" height="300" fill="var(--peach)"/>
  </svg>
  <div class="brand-name">Fennick Ranch</div>
  <div class="contact">
    <div class="person">Fennick Ranch Corin</div>
    <div class="detail">E-mail – fennickranch@mailbox-example.com</div>
    <div class="detail">Phone – 555 310-7282</div>
  </div>
  <div class="website">www.fennickranch-example.com</div>
</section>

<section class="card card--meadow">
  <svg class="card__frame" viewBox="0 0 520 300" aria-hidden="true">
    <rect width="520" height="300" fill="var(--maroon)"/>
  </svg>
  <div class="card__photo" role="img" aria-label="Photograph of sheep grazing on a green pasture"></div>
  <div class="brand-name">Fennick Ranch</div>
  <div class="person">Fennick Ranch Corin</div>
  <div class="detail-bar detail-bar--phone">Phone – 555 310-7282</div>
  <div class="detail-bar detail-bar--email">E-mail – fennickranch@mailbox-example.com</div>
  <div class="website">www.fennickranch-example.com</div>
</section>

</body>
</html>
```